Property Management business needs Business cards designed

We provide a premium property management service based in Sydney's Norther Beaches. We want people to feel confident in choosing us to manage their investment properties. We offer a much more personalized service than other estate agents.
We want a modern clean design. Something that shows confidence without being complicated.
Logo attached.

Target Market(s)

35-70yo Male and Female with strong property portfolios within Sydney's Norther Beaches

Industry/Entity Type

Property Management

Contact Information for Business Card

Address: Suite 7, 12-14 Kelvin Parade, Harlow NSW 2188
Two separate named cards.
Tom Ardley - 0491 570 118 tom@harbourvaleestates.com.au
Clara Dunmore - 0491 570 263 clara@harbourvaleestates.com.au

Requirements
Must have
• Business logo, name, number, address, email.

```html
<!DOCTYPE html>
<html lang="en">
<head>
<meta charset="utf-8">
<title>Harbourvale Estates – Business Cards</title>
<link href="https://fonts.googleapis.com/css2?family=Source+Sans+3:wght@400;600&display=swap" rel="stylesheet">
<style>
  :root {
    --backdrop: #e9e6e2;
    --card: #ffffff;
    --ink: #111111;
    --accent: #2a9aa3;
    --shadow: rgba(0, 0, 0, 0.28);
  }
  html, body {
    margin: 0;
    padding: 0;
    width: 1200px;
    height: 1000px;
    overflow: hidden;
    background: var(--backdrop);
    font-family: "Source Sans 3", "Myriad Pro", Arial, sans-serif;
    color: var(--ink);
  }
  .card {
    position: absolute;
    left: 265px;
    width: 666px;
    height: 398px;
    background: var(--card);
    box-shadow: 0 4px 10px var(--shadow);
  }
  .card--tom { top: 73px; }
  .card--clara { top: 532px; }

  .brand {
    position: absolute;
    right: 32px;
    top: 96px;
    display: flex;
    align-items: center;
    gap: 12px;
  }
  .brand__dot {
    width: 22px;
    height: 22px;
    border-radius: 50%;
    background: var(--accent);
  }
  .brand__name {
    font-size: 34px;
    font-weight: 600;
    letter-spacing: 0.2px;
    line-height: 1;
    text-transform: uppercase;
    color: var(--ink);
  }

  .person {
    position: absolute;
    left: 33px;
    right: 32px;
    top: 226px;
    margin: 0;
    padding-bottom: 10px;
    border-bottom: 1.5px solid var(--ink);
    font-size: 27px;
    font-weight: 600;
    line-height: 1.2;
  }

  .contact {
    position: absolute;
    left: 33px;
    top: 300px;
    margin: 0;
    padding: 0;
    list-style: none;
    font-size: 16.5px;
    line-height: 1;
  }
  .contact__item {
    display: flex;
    align-items: center;
    gap: 10px;
    height: 22px;
    margin-bottom: 9px;
  }
  .contact__icon {
    width: 14px;
    height: 14px;
    flex: none;
  }

  .address {
    position: absolute;
    right: 32px;
    top: 301px;
    margin: 0;
    font-style: normal;
    text-align: right;
    font-size: 16.5px;
    line-height: 25px;
  }
</style>
</head>
<body>

<section class="card card--tom">
  <div class="brand">
    <span class="brand__dot"></span>
    <span class="brand__name">Harbourvale Estates</span>
  </div>
  <h2 class="person">Tom Ardley</h2>
  <ul class="contact">
    <li class="contact__item">
      <svg class="contact__icon" viewBox="0 0 14 14" aria-hidden="true"><rect x="3.5" y="0.8" width="7" height="12.4" rx="1.2" fill="none" stroke="#111" stroke-width="1.3"/><line x1="6" y1="11" x2="8" y2="11" stroke="#111" stroke-width="1"/></svg>
      <span>0491 570 118</span>
    </li>
    <li class="contact__item">
      <svg class="contact__icon" viewBox="0 0 14 14" aria-hidden="true"><rect x="0.5" y="3" width="13" height="8.5" fill="#111"/><polyline points="0.8,3.4 7,8 13.2,3.4" fill="none" stroke="#fff" stroke-width="1"/></svg>
      <span>tom@harbourvaleestates.com.au</span>
    </li>
  </ul>
  <address class="address">Suite 7, 12-14 Kelvin Parade,<br>Harlow NSW 2188</address>
</section>

<section class="card card--clara">
  <div class="brand">
    <span class="brand__dot"></span>
    <span class="brand__name">Harbourvale Estates</span>
  </div>
  <h2 class="person">Clara Dunmore</h2>
  <ul class="contact">
    <li class="contact__item">
      <svg class="contact__icon" viewBox="0 0 14 14" aria-hidden="true"><rect x="3.5" y="0.8" width="7" height="12.4" rx="1.2" fill="none" stroke="#111" stroke-width="1.3"/><line x1="6" y1="11" x2="8" y2="11" stroke="#111" stroke-width="1"/></svg>
      <span>0491 570 263</span>
    </li>
    <li class="contact__item">
      <svg class="contact__icon" viewBox="0 0 14 14" aria-hidden="true"><rect x="0.5" y="3" width="13" height="8.5" fill="#111"/><polyline points="0.8,3.4 7,8 13.2,3.4" fill="none" stroke="#fff" stroke-width="1"/></svg>
      <span>clara@harbourvaleestates.com.au</span>
    </li>
  </ul>
  <address class="address">Suite 7, 12-14 Kelvin Parade,<br>Harlow NSW 2188</address>
</section>

</body>
</html>
```